We need a graphic design done for our Van. Something eye catching.

We would like the attached photo (file number 1) as our main picture on the side of the van. We would like “Silver Harbour Netball Institute” written either above or below.
The graphic design would be located on both sides of the van.

On the back window or van, we would like the other two pictures side by side.

our website is: www.shni-demo.com.au

```html
<!DOCTYPE html>
<html lang="en">
<head>
<meta charset="utf-8">
<title>Silver Harbour Netball Institute – Van Wrap Artwork</title>
<link href="https://fonts.googleapis.com/css2?family=Oswald:wght@400;500&display=swap" rel="stylesheet">
<style>
  :root {
    --paper: #ffffff;
    --brand-green: #3aa146;
    --brand-navy: #1f3d6b;
    --brand-teal: #2b7a78;
    --photo-dark: #2a3e55;
    --photo-mid: #3f6a7a;
    --photo-light: #7fb18a;
    --ink-light: #ffffff;
  }
  html, body {
    margin: 0;
    width: 1200px;
    height: 900px;
    overflow: hidden;
    background: var(--paper);
  }
  .artwork {
    display: block;
    width: 1200px;
    height: 900px;
    font-family: "Oswald", "Arial Narrow", sans-serif;
  }
  .headline { fill: var(--brand-green); font-weight: 500; font-size: 48px; }
  .subline { fill: var(--brand-green); font-weight: 400; font-size: 22px; }
  .contact { fill: var(--ink-light); font-weight: 400; font-size: 22px; }
  .contact-web { fill: var(--ink-light); font-weight: 400; font-size: 18px; }
  .brand-name { fill: var(--ink-light); font-weight: 400; font-size: 22px; letter-spacing: 1px; }
</style>
</head>
<body>
<svg class="artwork" viewBox="0 0 1200 900" xmlns="http://www.w3.org/2000/svg">
  <defs>
    <linearGradient id="band-gradient" x1="0" y1="0" x2="1" y2="0">
      <stop offset="0" stop-color="var(--brand-navy)"/>
      <stop offset="0.5" stop-color="var(--brand-teal)"/>
      <stop offset="1" stop-color="var(--brand-green)"/>
    </linearGradient>
    <linearGradient id="thin-band-gradient" x1="0" y1="0" x2="1" y2="0">
      <stop offset="0" stop-color="var(--brand-navy)"/>
      <stop offset="1" stop-color="var(--brand-teal)"/>
    </linearGradient>
    <linearGradient id="photo-gradient" x1="0" y1="0" x2="1" y2="1">
      <stop offset="0" stop-color="var(--photo-light)"/>
      <stop offset="0.5" stop-color="var(--photo-mid)"/>
      <stop offset="1" stop-color="var(--photo-dark)"/>
    </linearGradient>

    <g id="brand-panel">
      <polygon class="band-thin" points="30,130 380,26 380,42 30,146" fill="url(#thin-band-gradient)"/>
      <polygon class="band-main" points="0,330 460,194 460,284 0,420" fill="url(#band-gradient)"/>
      <text class="headline" x="40" y="220" transform="rotate(-16.5 40 220)">SILVER HARBOUR</text>
      <text class="subline" x="80" y="252" transform="rotate(-16.5 80 252)">NETBALL INSTITUTE</text>
      <text class="contact" x="60" y="346" transform="rotate(-16.5 60 346)">0400 123 456</text>
      <text class="contact-web" x="80" y="372" transform="rotate(-16.5 80 372)">shni-demo.com.au</text>
      <circle class="brand-dot" cx="272" cy="292" r="7" fill="var(--ink-light)"/>
      <text class="brand-name" x="288" y="298" transform="rotate(-16.5 288 298)">SHNI</text>
    </g>
  </defs>

  <g class="wrap-side wrap-side--passenger" transform="translate(50 40)">
    <rect class="action-photo" x="20" y="20" width="300" height="370" rx="6" fill="url(#photo-gradient)" role="img" aria-label="Action photo of two players in training, one carrying the ball towards a teammate holding a tackle pad"/>
    <use href="#brand-panel" x="300" y="0"/>
  </g>

  <g class="wrap-side wrap-side--driver" transform="translate(50 460)">
    <use href="#brand-panel" x="360" y="0"/>
    <rect class="action-photo" x="800" y="20" width="300" height="370" rx="6" fill="url(#photo-gradient)" role="img" aria-label="Action photo of two players in training, one carrying the ball towards a teammate holding a tackle pad"/>
  </g>
</svg>
</body>
</html>
```